eBook Lumio

I currently use the free eBook app Lumio avail from tolvex

I would like an app to be developed the same but with the following options

But I would like an option in my book listing to mark off the books I've already read.

Maybe also an option to rate the book as well.

Option to choose different bookshelves
Like a nice white beachy looking one
Dark timber very formal
Colourful funky

Target Market(s)

All readers who love to carry all there books with them

Requirements
Must have
• Similar bookshelf look
Either be able to list books or show thumbnail of books
Epub and PDF format
Able to sort by Titles, Author or Catergories
Must have a search field
Nice to have
• Option to choose different bookshelves
Dark timber very formal
Colourful funky

```html
<!DOCTYPE html>
<html lang="en">
<head>
<meta charset="utf-8">
<title>NameApp – Bookshelf</title>
<link href="https://fonts.googleapis.com/css2?family=Nunito:wght@800&family=Cinzel:wght@400&display=swap" rel="stylesheet">
<style>
  :root {
    --stage: #e3e4e6;
    --header-top: #4d586c;
    --header-bottom: #1c2330;
    --header-edge: #0e131b;
    --icon: #b9bec6;
    --title: #ffffff;
    --wood-light: #7a3f22;
    --wood-mid: #5e2e18;
    --wood-dark: #3a1c0e;
    --wood-floor: #24130a;
    --shelf-top: #e6b884;
    --shelf-face: #c98d55;
    --shelf-edge: #9a6233;
    --cover-top: #8a8f94;
    --cover-bottom: #3d3a34;
    --cover-text: #e9dfc4;
    --badge: #2f8ed8;
    --tick: #35d63c;
  }
  * { box-sizing: border-box; margin: 0; padding: 0; }
  html, body {
    width: 1200px; height: 848px; overflow: hidden;
    background: var(--stage);
  }
  .app-screen {
    position: absolute; left: 343px; top: 26px;
    width: 521px; height: 798px;
    box-shadow: 0 0 12px rgba(0,0,0,0.25);
    overflow: hidden;
  }
  .app-header {
    position: relative; height: 74px;
    background: linear-gradient(var(--header-top), var(--header-bottom));
    border-bottom: 3px solid var(--header-edge);
    display: flex; align-items: center; justify-content: center;
    z-index: 2;
  }
  .app-title {
    font-family: "Nunito", sans-serif; font-weight: 800;
    font-size: 34px; color: var(--title); letter-spacing: 0.5px;
  }
  .header-icon { position: absolute; top: 17px; width: 38px; height: 38px; }
  .header-icon.home { left: 16px; }
  .header-icon.settings { right: 16px; }
  .bookcase {
    position: absolute; top: 74px; left: 0; right: 0; bottom: 0;
    background:
      linear-gradient(to bottom, transparent 0, transparent 598px, var(--wood-floor) 640px),
      radial-gradient(ellipse at 50% 0%, var(--wood-light) 0%, var(--wood-mid) 45%, var(--wood-dark) 100%);
  }
  .shelf {
    position: absolute; left: 10px; right: 8px; height: 30px;
  }
  .shelf-top {
    height: 8px; background: var(--shelf-top);
    clip-path: polygon(2% 0, 98% 0, 100% 100%, 0 100%);
  }
  .shelf-face {
    height: 18px;
    background: linear-gradient(var(--shelf-face), var(--shelf-edge));
    box-shadow: 0 6px 8px rgba(0,0,0,0.45);
  }
  .shelf-1 { top: 126px; }
  .shelf-2 { top: 266px; }
  .shelf-3 { top: 408px; }
  .shelf-4 { top: 548px; }
  .book {
    position: absolute; left: 37px; top: 166px;
    width: 94px; height: 112px;
    box-shadow: 2px 2px 4px rgba(0,0,0,0.5);
  }
  .book-cover {
    position: absolute; inset: 0;
    background: linear-gradient(var(--cover-top), var(--cover-bottom));
  }
  .book-title {
    position: absolute; left: 0; right: 0; bottom: 6px;
    font-family: "Cinzel", serif; font-size: 11px; line-height: 1.15;
    color: var(--cover-text); text-align: center;
  }
  .book-badge {
    position: absolute; left: 0; top: 10px;
    width: 56px; height: 14px; background: var(--badge);
    font-family: "Nunito", sans-serif; font-weight: 800;
    font-size: 9px; color: #fff; padding-left: 10px; line-height: 14px;
  }
  .book-tick { position: absolute; right: -8px; top: 18px; width: 26px; height: 22px; }
</style>
</head>
<body>
  <main class="app-screen">
    <header class="app-header">
      <svg class="header-icon home" viewBox="0 0 24 24" aria-label="Home">
        <path d="M12 3 L2 12 H5 V21 H10 V15 H14 V21 H19 V12 H22 Z" fill="var(--icon)"/>
      </svg>
      <h1 class="app-title">NameApp</h1>
      <svg class="header-icon settings" viewBox="0 0 24 24" aria-label="Settings">
        <path fill="var(--icon)" fill-rule="evenodd" d="M10 1h4l.6 3a8 8 0 0 1 2.2 1.3l2.9-1 2 3.4-2.3 2a8 8 0 0 1 0 2.6l2.3 2-2 3.4-2.9-1a8 8 0 0 1-2.2 1.3L14 23h-4l-.6-3a8 8 0 0 1-2.2-1.3l-2.9 1-2-3.4 2.3-2a8 8 0 0 1 0-2.6l-2.3-2 2-3.4 2.9 1A8 8 0 0 1 9.4 4Z M12 8.5a3.5 3.5 0 1 0 0 7a3.5 3.5 0 1 0 0-7Z"/>
      </svg>
    </header>
    <section class="bookcase">
      <div class="shelf shelf-1"><div class="shelf-top"></div><div class="shelf-face"></div></div>
      <div class="shelf shelf-2"><div class="shelf-top"></div><div class="shelf-face"></div></div>
      <div class="shelf shelf-3"><div class="shelf-top"></div><div class="shelf-face"></div></div>
      <div class="shelf shelf-4"><div class="shelf-top"></div><div class="shelf-face"></div></div>
      <article class="book">
        <div class="book-cover" role="img" aria-label="Book cover illustration"></div>
        <div class="book-badge">New</div>
        <p class="book-title">A GARDEN<br>IN JUNE<br>E. L. MARLOW</p>
        <svg class="book-tick" viewBox="0 0 26 22" aria-label="Read">
          <path d="M2 12 L9 19 L24 3" fill="none" stroke="var(--tick)" stroke-width="5" stroke-linecap="round" stroke-linejoin="round"/>
        </svg>
      </article>
    </section>
  </main>
</body>
</html>
```